Dinewell - Slate App Design Project

I have a Slate app that serves as a restaurant reservation system. The design that i currently have is very basic apple design. I am looking for it to have a much more professional appeal.

Please review the attached document which contains all of the screen shots for the app.
Updates

This Project has now been Guaranteed.  I look forward to reviewing your designs.

Brent

Reason: I am extending my deadline because i just changed this contest to guaranteed and have received a ton more "acceptances" because of it and I want to give those designers a chance to submit a design.

Target Market(s)

restaurant owners

Industry/Entity Type

Restaurant

Requirements
Must have
• On the seating chart i am changing the feature that shows the tables highlighted and instead would like that replace with a badge. So the list of wait staff across the top of the seating chart would instead have a number next to their name and would correspond with the badge on the table to determine their section.

So for example:
Ada would have a number 1 in front of her name and tables 18, 19, 20, and 31 would have a little badge in the upper right hand corner with the number "1" inside the badge.
Uma would have a number 2 in front of her name and tables 6, 7, and 11 would have a little badge in the upper right hand corner with the number " 2" inside the badge.
Nora would have a number 3 in front of her name and tables 12, 13, 27, 28, 29, and 30 would have a little badge in the upper right hand corner with the number " 3" inside the badge.

The names on the top will all be ONE color

Also, i would like an icon developed to replace the "C" you see next to some of the people's name in the reservation and waitlist slots. Also, i would like a better looking "check mark".

```html
<!DOCTYPE html>
<html lang="en">
<head>
<meta charset="utf-8">
<title>Dinewell – Host Stand</title>
<link href="https://fonts.googleapis.com/css2?family=Arimo:ital,wght@0,400;0,700;1,400&display=swap" rel="stylesheet">
<style>
:root{
  --page:#3a3a3c;
  --body:#2a2a2c;
  --status:#0c0c0c;
  --nav-top:#a9dcf8;
  --nav-bot:#5db4e8;
  --btn-top:#8fd2f7;
  --btn-bot:#4aa6e0;
  --btn-line:#2b7fb8;
  --ink:#1e1e1e;
  --muted:#9a9a9a;
  --accent:#3ea8ea;
  --alert:#e81c1c;
  --card:#ffffff;
  --rule:#dddddd;
  --head-top:#ececec;
  --head-bot:#cdcdcd;
  --stat-line:#5a5a5e;
  --ok-off:#a8a8a8;
}
*{box-sizing:border-box;margin:0;padding:0}
html,body{width:1200px;height:1029px;overflow:hidden;background:var(--page);font-family:"Arimo",Arial,sans-serif}
.screen{position:absolute;top:64px;left:0;width:1200px;height:900px;background:var(--body);overflow:hidden}
.status{height:23px;background:var(--status);color:#fff;font-size:13px;display:flex;align-items:center;padding:0 8px;position:relative}
.status .clock{position:absolute;left:0;right:0;text-align:center;font-weight:700}
.status .device{display:flex;align-items:center;gap:6px}
.status .battery{margin-left:auto;display:flex;align-items:center;gap:5px;font-size:12px}
.nav{height:51px;background:linear-gradient(var(--nav-top),var(--nav-bot));position:relative;border-bottom:1px solid #3a8cc4}
.nav .btn{position:absolute;top:7px;height:35px;border:1px solid var(--btn-line);border-radius:5px;background:linear-gradient(var(--btn-top),var(--btn-bot));font-size:15px;font-weight:700;color:#0e2c44;display:flex;align-items:center;justify-content:center;box-shadow:inset 0 1px 0 rgba(255,255,255,.6)}
.nav .btn.light{background:linear-gradient(#eef4f8,#b8c6d2);border-color:#7f93a4;font-weight:400;color:#222}
.brand{position:absolute;left:0;right:0;top:9px;text-align:center;color:#fff;font-size:31px;letter-spacing:1px}
.stats{position:absolute;top:90px;left:0;width:1200px;height:46px}
.stat{position:absolute;top:0;height:46px;border:1px solid var(--stat-line);border-radius:3px;background:#232325;color:#fff;text-align:center;font-size:13px;line-height:19px;padding-top:3px}
.stat b{display:block;font-weight:400;color:var(--accent)}
.stat.when{font-size:22px;color:#cfcfcf;line-height:40px;padding:0 10px;text-align:left}
.waitlist{position:absolute;left:15px;top:156px;width:357px;bottom:0;background:var(--card)}
.waitlist .head{height:61px;background:linear-gradient(#8fd0f6,#4ea9e2);color:#fff;text-align:center;position:relative}
.waitlist .head h2{font-size:22px;font-weight:400;padding-top:6px}
.waitlist .head p{font-size:17px;font-style:italic;color:#1c3d58}
.waitlist .head:after{content:"";position:absolute;left:50%;bottom:-7px;margin-left:-8px;border:8px solid transparent;border-bottom:0;border-top:7px solid #4ea9e2}
.party{height:59.5px;border-bottom:1px solid var(--rule);padding:9px 12px 0 17px}
.party .line{display:flex;align-items:baseline;font-size:18px;color:var(--ink);white-space:nowrap}
.party .line .dots{flex:1;border-bottom:1px dotted #444;margin:0 2px;transform:translateY(-4px)}
.party .line .due.late{color:var(--alert)}
.party small{display:block;font-size:13px;color:var(--muted);margin-top:1px}
.party small b{font-weight:400;color:var(--accent)}
.col{position:absolute;top:156px;width:383px;display:flex;flex-direction:column;gap:15px}
.col.mid{left:394px}
.col.right{left:797px}
.slot{background:var(--card)}
.slot .top{height:35px;background:linear-gradient(var(--head-top),var(--head-bot));display:grid;grid-template-columns:120px 1fr 50px 40px;align-items:center;padding-left:17px;color:#333}
.slot .top .time{font-size:18px}
.slot .top .tag{font-size:13px}
.slot .top .tag.full{color:var(--alert);font-weight:700}
.slot .top .hdr{font-size:13px}
.slot .top svg{width:20px;height:20px}
.res{height:44px;border-bottom:1px solid var(--rule);display:grid;grid-template-columns:1fr auto 46px 47px;align-items:center;position:relative}
.res:last-child{border-bottom:0}
.res .who{padding-left:10px;align-self:stretch;display:flex;flex-direction:column;justify-content:center;line-height:1.15;min-width:0}
.res .name{font-size:18px;color:var(--ink);white-space:nowrap}
.res .note{font-size:12.5px;font-style:italic;color:var(--ink);white-space:nowrap;overflow:visible;width:0}
.res.two .marks,.res.two .size{align-self:start;padding-top:6px}
.res.pending .name{color:var(--muted)}
.res.pending .note{color:var(--muted)}
.res .marks{display:flex;align-items:center;gap:6px;padding-right:4px}
.res.two .marks{padding-top:10px}
.res .size{font-size:18px;text-align:center;color:var(--ink)}
.res.pending .size,.res.pending .tbl{color:var(--muted)}
.res .tbl{height:100%;border-left:1px solid var(--rule);display:flex;align-items:center;justify-content:center;font-size:18px}
.res.two .tbl{align-items:flex-start;padding-top:6px}
.ok{display:inline-block;width:24px;height:13px;border-radius:7px;background:var(--accent);color:#fff;font-size:9px;font-weight:700;font-style:normal;text-align:center;line-height:13px}
.ok.off{background:var(--ok-off)}
.guest{width:23px;height:14px;fill:var(--ok-off)}
.guest.on{fill:var(--accent)}
</style>
</head>
<body>
<svg width="0" height="0" style="position:absolute">
  <symbol id="guests" viewBox="0 0 23 14"><circle cx="7" cy="4" r="3.3"/><path d="M1 14c0-4.5 2.7-6.5 6-6.5s6 2 6 6.5z"/><circle cx="16" cy="4" r="3.3"/><path d="M10 14c0-4.5 2.7-6.5 6-6.5s6 2 6 6.5z"/></symbol>
  <symbol id="plus" viewBox="0 0 20 20"><path d="M8 1h4v7h7v4h-7v7H8v-7H1V8h7z" fill="#1b1b1b"/></symbol>
</svg>

<main class="screen">
  <header class="status">
    <span class="device">Slate
      <svg width="16" height="12" viewBox="0 0 16 12"><path d="M8 11l2-2.4a3 3 0 0 0-4 0zM3.5 6a6.5 6.5 0 0 1 9 0l-1.3 1.5a4.5 4.5 0 0 0-6.4 0zM1 3.2a10 10 0 0 1 14 0l-1.3 1.5a8 8 0 0 0-11.4 0z" fill="#fff"/></svg>
    </span>
    <span class="clock">10:50 AM</span>
    <span class="battery">41 %
      <svg width="24" height="12" viewBox="0 0 24 12"><rect x=".5" y=".5" width="20" height="11" rx="1.5" fill="none" stroke="#fff"/><rect x="21" y="3.5" width="2" height="5" fill="#fff"/><rect x="2" y="2" width="8" height="8" fill="#fff"/></svg>
    </span>
  </header>

  <nav class="nav">
    <span class="btn" style="left:15px;width:131px">Seating Chart</span>
    <span class="btn" style="left:163px;width:129px">Specials</span>
    <span class="btn" style="left:308px;width:131px">Staff Notes</span>
    <div class="brand">Dinewell</div>
    <span class="btn" style="left:907px;width:132px">Calendar</span>
    <span class="btn light" style="left:1054px;width:131px">Management</span>
  </nav>

  <section class="stats">
    <div class="stat when" style="left:15px;width:245px">2:17 PM, Mon Sep 10</div>
    <div class="stat" style="left:280px;width:149px">Avg Wait Time<b>25 mins</b></div>
    <div class="stat" style="left:444px;width:150px">Open Tables<b>66</b></div>
    <div class="stat" style="left:610px;width:196px">Checked In<b>14 Groups - 56 people</b></div>
    <div class="stat" style="left:823px;width:176px">Currently Seated<b>11/296</b></div>
    <div class="stat" style="left:1012px;width:174px">Open Reservations<b>370 People</b></div>
  </section>

  <aside class="waitlist">
    <div class="head"><h2>Wait List</h2><p>Add a party to the wait list ...</p></div>
    <div class="party"><div class="line">Clara Hobbs<span class="dots"></span><span class="due late">5m (2:02 PM)</span></div><small>Party of <b>4</b></small></div>
    <div class="party"><div class="line">Brent Colby<span class="dots"></span><span class="due late">5m (2:02 PM)</span></div><small>Party of <b>2</b></small></div>
    <div class="party"><div class="line">Rhea Lund<span class="dots"></span><span class="due">25m (2:22 PM)</span></div><small>Party of <b>4</b></small></div>
    <div class="party"><div class="line">Mira Castell<span class="dots"></span><span class="due">25m (2:23 PM)</span></div><small>Party of <b>3</b></small></div>
    <div class="party"><div class="line">Selena Varga-Holt<span class="dots"></span><span class="due">30m (2:28 PM)</span></div><small>Party of <b>4</b></small></div>
    <div class="party"><div class="line">Oona Field<span class="dots"></span><span class="due">30m (2:28 PM)</span></div><small>Party of <b>6</b></small></div>
    <div class="party"><div class="line">Petra Holm<span class="dots"></span><span class="due">30m (2:28 PM)</span></div><small>Party of <b>6</b></small></div>
    <div class="party"><div class="line">Ines Marlowe<span class="dots"></span><span class="due late">15m (2:14 PM)</span></div><small>Party of <b>4</b></small></div>
    <div class="party"><div class="line">Hugo Penn<span class="dots"></span><span class="due">40m (2:39 PM)</span></div><small>Party of <b>5</b></small></div>
    <div class="party"></div>
    <div class="party"></div>
  </aside>

  <section class="col mid">
    <div class="slot">
      <div class="top"><span class="time">12:00 PM</span><span class="tag">9/22</span><span class="hdr">Size</span><svg><use href="#plus"/></svg></div>
      <div class="res pending two"><div class="who"><span class="name">Ned Crane</span><span class="note">I would like a booth in the corner</span></div><span class="marks"><i class="ok off">OK</i></span><span class="size">4</span><span class="tbl">11</span></div>
      <div class="res"><div class="who"><span class="name">Ada Quill</span></div><span class="marks"><i class="ok">OK</i></span><span class="size">3</span><span class="tbl"></span></div>
      <div class="res pending two"><div class="who"><span class="name">Otto Reyes</span><span class="note">Patio table if available</span></div><span class="marks"><svg class="guest"><use href="#guests"/></svg></span><span class="size">2</span><span class="tbl">1</span></div>
    </div>
    <div class="slot">
      <div class="top"><span class="time">12:15 PM</span><span class="tag full">Full</span><span class="hdr">Size</span><svg><use href="#plus"/></svg></div>
      <div class="res"><div class="who"><span class="name">Leon Marsh</span></div><span class="marks"><i class="ok">OK</i></span><span class="size">4</span><span class="tbl"></span></div>
      <div class="res pending two"><div class="who"><span class="name">Rolf Adler</span><span class="note">Birthday celebration</span></div><span class="marks"><svg class="guest"><use href="#guests"/></svg><i class="ok off">OK</i></span><span class="size">5</span><span class="tbl">12</span></div>
      <div class="res two"><div class="who"><span class="name">Ivo Brandt</span><span class="note">We have one person that needs gluten free food</span></div><span class="marks"><i class="ok">OK</i></span><span class="size">2</span><span class="tbl"></span></div>
      <div class="res"><div class="who"><span class="name">Cal Everly</span></div><span class="marks"></span><span class="size">4</span><span class="tbl"></span></div>
    </div>
    <div class="slot">
      <div class="top"><span class="time">12:00 PM</span><span class="tag">9/22</span><span class="hdr">Size</span><svg><use href="#plus"/></svg></div>
      <div class="res pending two"><div class="who"><span class="name">Ned Crane</span><span class="note">I would like a booth in the corner</span></div><span class="marks"><i class="ok off">OK</i></span><span class="size">4</span><span class="tbl">11</span></div>
      <div class="res"><div class="who"><span class="name">Ada Quill</span></div><span class="marks"><i class="ok">OK</i></span><span class="size">3</span><span class="tbl"></span></div>
      <div class="res pending two"><div class="who"><span class="name">Otto Reyes</span><span class="note">Patio table if available</span></div><span class="marks"><svg class="guest"><use href="#guests"/></svg></span><span class="size">2</span><span class="tbl">1</span></div>
    </div>
    <div class="slot">
      <div class="top"><span class="time">12:00 PM</span><span class="tag">9/22</span><span class="hdr">Size</span><svg><use href="#plus"/></svg></div>
      <div class="res pending two"><div class="who"><span class="name">Ned Crane</span><span class="note">I would like a booth in the corner</span></div><span class="marks"><i class="ok off">OK</i></span><span class="size">4</span><span class="tbl">11</span></div>
      <div class="res"><div class="who"><span class="name">Ada Quill</span></div><span class="marks"><svg class="guest on"><use href="#guests"/></svg><i class="ok">OK</i></span><span class="size">3</span><span class="tbl"></span></div>
    </div>
  </section>

  <section class="col right">
    <div class="slot">
      <div class="top"><span class="time">12:15 PM</span><span class="tag full">Full</span><span class="hdr">Size</span><svg><use href="#plus"/></svg></div>
      <div class="res"><div class="who"><span class="name">Leon Marsh</span></div><span class="marks"><i class="ok">OK</i></span><span class="size">4</span><span class="tbl"></span></div>
      <div class="res pending two"><div class="who"><span class="name">Rolf Adler</span><span class="note">Birthday celebration</span></div><span class="marks"><svg class="guest"><use href="#guests"/></svg><i class="ok off">OK</i></span><span class="size">5</span><span class="tbl">12</span></div>
      <div class="res two"><div class="who"><span class="name">Ivo Brandt</span><span class="note">We have one person that needs gluten free food</span></div><span class="marks"><i class="ok">OK</i></span><span class="size">2</span><span class="tbl"></span></div>
      <div class="res"><div class="who"><span class="name">Cal Everly</span></div><span class="marks"></span><span class="size">4</span><span class="tbl"></span></div>
    </div>
    <div class="slot">
      <div class="top"><span class="time">12:00 PM</span><span class="tag">9/22</span><span class="hdr">Size</span><svg><use href="#plus"/></svg></div>
      <div class="res pending two"><div class="who"><span class="name">Ned Crane</span><span class="note">I would like a booth in the corner</span></div><span class="marks"><i class="ok off">OK</i></span><span class="size">4</span><span class="tbl">11</span></div>
      <div class="res"><div class="who"><span class="name">Ada Quill</span></div><span class="marks"><i class="ok">OK</i></span><span class="size">3</span><span class="tbl"></span></div>
      <div class="res pending two"><div class="who"><span class="name">Otto Reyes</span><span class="note">Patio table if available</span></div><span class="marks"><svg class="guest"><use href="#guests"/></svg></span><span class="size">2</span><span class="tbl">1</span></div>
    </div>
    <div class="slot">
      <div class="top"><span class="time">12:15 PM</span><span class="tag full">Full</span><span class="hdr">Size</span><svg><use href="#plus"/></svg></div>
      <div class="res"><div class="who"><span class="name">Leon Marsh</span></div><span class="marks"><i class="ok">OK</i></span><span class="size">4</span><span class="tbl"></span></div>
      <div class="res pending two"><div class="who"><span class="name">Rolf Adler</span><span class="note">Birthday celebration</span></div><span class="marks"><svg class="guest"><use href="#guests"/></svg><i class="ok off">OK</i></span><span class="size">5</span><span class="tbl">12</span></div>
      <div class="res two"><div class="who"><span class="name">Ivo Brandt</span><span class="note">We have one person that needs gluten free food</span></div><span class="marks"><i class="ok">OK</i></span><span class="size">2</span><span class="tbl"></span></div>
      <div class="res"><div class="who"><span class="name">Cal Everly</span></div><span class="marks"></span><span class="size">4</span><span class="tbl"></span></div>
    </div>
    <div class="slot">
      <div class="top"><span class="time">12:00 PM</span><span class="tag">9/22</span><span class="hdr">Size</span><svg><use href="#plus"/></svg></div>
      <div class="res pending two"><div class="who"><span class="name">Ned Crane</span><span class="note">I would like a booth in the corner</span></div><span class="marks"><i class="ok off">OK</i></span><span class="size">4</span><span class="tbl">11</span></div>
    </div>
  </section>
</main>
</body>
</html>
```